Website Landing Page for Brightfall Systems

Create a custom designed website landing page for our business. Looking for a professional upscale design that incorporates our logo and logo colors into the theme. I want a standard fixed frame website, not a constant scrolling format that seems to be the trend. To start with I'm looking for more of the graphic design part, maybe a concept or theme, I don't expect to see a finished project. Not interested in generic templates or layouts.

The name of our company is Brightfall Systems and I've attached our logo below. I'd like to have the web page have the same look and feel of our logo, as well as the colors. Our company, Brightfall Systems does system design, installation, and programming, of residential and commercial Audio/Video and Automation systems. We do home theaters, lighting and building automation, video conferencing systems, security camera installations, conference rooms, projectors, distributed audio systems, and similar Technology projects. This will be a professional services/informational website. We will not sell products on this website. This website will be used to advertise our company and communicate our services to prospective customers. Having a well designed, professional and clean website is one way we want to distinguish our company from the competition.

Here are some examples of what I consider a professional well designed website
http://www.qorlamstudio.com/Work/

Last year we had our tradlo store designed (with PixelMarket) and I'm really happy with the way it turned out. You can see it at www.HolvenGearDepot.com I consider this to be a great design and looking for the same level of quality with this new website. However, do not copy or use any part of this design in this new project. This tradlo store is completely separate from our other company Brightfall Systems. I only mention this tradlo store an an example of good work.

Reason: Still going through designs.

Reason: Still working on project and have not had time to review all designs and request revisions.

Reason: Sill going through designs and requesting revisions

Reason: still going through all the submissions we received.

Target Market(s)

People interested in Audio/Video, home theaters, home automation. We do sales, system design, and programming. We typically work on larger projects with both residential and commercial customers.

Industry/Entity Type

Business

Number of Pages Required

1 page

Requirements
Must have
• Great design elements. Please use a white background. I think white goes well with our logo colors.

```html
<!DOCTYPE html>
<html lang="en">
<head>
<meta charset="utf-8">
<title>Brightfall Systems — Landing Page</title>
<link rel="stylesheet" href="https://fonts.googleapis.com/css2?family=Roboto:wght@300;400;500&display=swap">
<style>
  :root {
    --canvas: #f2f3f5;
    --white: #ffffff;
    --ink: #2b2b2b;
    --ink-soft: #5c5f66;
    --brand-blue: #2a7de1;
    --brand-green: #4cb050;
    --green-band: #47ad4c;
    --hero-bg: #eceef1;
    --rule: #e3e5e8;
    --footer-bg: #f8f9fa;
    --muted: #8a8f96;
  }
  * { box-sizing: border-box; margin: 0; padding: 0; }
  html, body { width: 1200px; height: 1200px; overflow: hidden; }
  body {
    background: var(--canvas);
    font-family: "Roboto", Arial, sans-serif;
    color: var(--ink);
    position: relative;
  }
  .page {
    position: absolute;
    left: 0; top: 237px;
    width: 1200px; height: 725px;
    background: var(--white);
    overflow: hidden;
  }

  /* Header */
  .site-header {
    position: absolute; left: 0; top: 0;
    width: 100%; height: 97px;
    background: var(--white);
    border-bottom: 1px solid var(--rule);
  }
  .brand {
    position: absolute; left: 106px; top: 17px;
    display: flex; align-items: center; gap: 16px;
  }
  .brand-mark {
    width: 62px; height: 62px; border-radius: 50%;
    border: 4px solid var(--brand-blue);
  }
  .brand-name {
    font-size: 24px; font-weight: 500; letter-spacing: 0.5px;
    text-transform: uppercase; color: var(--brand-blue);
  }
  .main-nav a {
    position: absolute; top: 40px;
    font-size: 13px; color: var(--ink); text-decoration: none;
  }
  .main-nav a.is-active::after {
    content: ""; position: absolute; left: -3px; right: -3px; top: 38px;
    height: 2px; background: var(--brand-green);
  }
  .social-links {
    position: absolute; left: 1072px; top: 44px;
    display: flex; gap: 10px;
  }
  .social-links span {
    width: 8px; height: 8px; border-radius: 50%;
    background: var(--brand-blue);
  }

  /* Hero */
  .hero {
    position: absolute; left: 0; top: 97px;
    width: 100%; height: 274px;
    background: linear-gradient(135deg, #f1f2f4 0%, var(--hero-bg) 55%, #f3f4f6 100%);
    text-align: center;
  }
  .hero-title {
    position: absolute; left: 0; right: 0; top: 62px;
    font-size: 34px; font-weight: 300; line-height: 41px;
    color: var(--ink);
  }
  .hero-title .soft { color: var(--ink-soft); }
  .cta {
    position: absolute; left: 477px; top: 166px;
    width: 246px; height: 57px; border-radius: 29px;
    background: var(--brand-blue); color: var(--white);
    font-size: 16px; font-weight: 400;
    display: flex; align-items: center; justify-content: center; gap: 14px;
    text-decoration: none;
    box-shadow: 0 2px 6px rgba(42,125,225,0.3);
  }

  /* Project showcase */
  .showcase {
    position: absolute; left: 0; top: 371px;
    width: 100%; height: 261px;
    background: var(--green-band);
  }
  .project {
    position: absolute; top: 26px; height: 209px;
  }
  .project-theater { left: 67px; width: 335px; background: linear-gradient(160deg, #9c9a96, #4d4c4a 60%, #2c2d33); }
  .project-living { left: 430px; width: 339px; background: linear-gradient(170deg, #e9d6a8, #c9a878 50%, #8c7456); }
  .project-office { left: 791px; width: 342px; background: linear-gradient(140deg, #2c5fb0, #6d98d6 55%, #c4d5ea); }
  .slider-arrow {
    position: absolute; top: 118px; width: 22px; height: 26px;
  }
  .slider-prev { left: 34px; }
  .slider-next { left: 1164px; }

  /* Footer */
  .band-gap {
    position: absolute; left: 0; top: 632px;
    width: 100%; height: 38px;
    background: var(--footer-bg);
    border-bottom: 1px solid var(--rule);
  }
  .site-footer {
    position: absolute; left: 0; top: 671px;
    width: 100%; height: 54px;
    text-align: center; font-size: 10px; color: var(--muted);
    padding-top: 21px;
  }
</style>
</head>
<body>
  <main class="page">
    <header class="site-header">
      <div class="brand">
        <span class="brand-mark"></span>
        <span class="brand-name">Brightfall Systems</span>
      </div>
      <nav class="main-nav">
        <a href="#" style="left:537px">Services</a>
        <a href="#" style="left:627px">Work</a>
        <a href="#" class="is-active" style="left:714px">About</a>
        <a href="#" style="left:798px">Contact</a>
        <a href="#" style="left:879px">Start a Project</a>
      </nav>
      <div class="social-links" aria-label="Social links">
        <span></span><span></span><span></span><span></span><span></span>
      </div>
    </header>

    <section class="hero">
      <h1 class="hero-title">
        System design, installation, and programming, of <span class="soft">residential and</span><br>
        commercial Audio/Video and Automation <span class="soft">systems</span>
      </h1>
      <a href="#" class="cta">Discover more <span>&rarr;</span></a>
    </section>

    <section class="showcase">
      <svg class="slider-arrow slider-prev" viewBox="0 0 22 26" aria-hidden="true">
        <polyline points="16,3 6,13 16,23" fill="none" stroke="#ffffff" stroke-width="5"/>
      </svg>
      <div class="project project-theater" role="img" aria-label="Auditorium with tiered seating and a projection screen"></div>
      <div class="project project-living" role="img" aria-label="Living room with home theater screen and ceiling projector"></div>
      <div class="project project-office" role="img" aria-label="Glass office building against a blue sky"></div>
      <svg class="slider-arrow slider-next" viewBox="0 0 22 26" aria-hidden="true">
        <polyline points="6,3 16,13 6,23" fill="none" stroke="#ffffff" stroke-width="5"/>
      </svg>
    </section>

    <div class="band-gap"></div>
    <footer class="site-footer">© Copyright 2017 &nbsp;Northlane Studio, All Rights Reserved</footer>
  </main>
</body>
</html>
```